Website design for Maple Nook Kidcare

I need a website designed for my daycare business, Maple Nook Kidcare, now that I have a new logo. My former website was ok but simple and I did not have a logo yet. It also was created by me using a template and was entirely pink. I loved the bright, happy feel of it but worried it might not appeal as much to potential clients who have sons. Therefore, I need a site which will appeal to both genders while still keeping the cheerful color scheme of my new logo, which has pinks, blue, green and cream.

Reason: Hello! I am still trying to download my new logo and am sorry it is taking me so long. Hopefully I will it posted by the end of today (US Eastern Standard Time). Thank you all very much for your patience!

Hello! I have finally managed to upload my new logo for you to use in designing my website. I'm sorry it took so long and greatly appreciate your time and creative efforts! I look forward to seeing what is submitted based on my logo design and its style/colors.

Many thanks!

Reason: As I've been traveling and posted my logo file late, I am extending my deadline. I am now back and can focus on providing more and better feedback. I appreciate your patience and submissions very much!

Reason: I need more time to provide feedback and make decisions.

Industry/Entity Type

Daycare

Colors
0192cd
33a6d7
86cae7
cadf82
fbf289
add136
e34197

```html
<!DOCTYPE html>
<html lang="en">
<head>
<meta charset="utf-8">
<title>Maple Nook Kidcare</title>
<link href="https://fonts.googleapis.com/css2?family=Open+Sans:wght@400;600;700&display=swap" rel="stylesheet">
<style>
:root{
  --blue-deep:#0192cd;
  --blue:#33a6d7;
  --blue-soft:#86cae7;
  --sky-top:#2f9be0;
  --sky-low:#bfe4f6;
  --lime:#add136;
  --lime-soft:#cadf82;
  --grass:#7fb52c;
  --grass-dark:#5e9320;
  --yellow:#fbf289;
  --nav:#e6e43a;
  --pink:#e34197;
  --orange:#f29a1f;
  --orange-dark:#e5731c;
  --teal:#1fae9c;
  --gold:#f5c64a;
  --ink:#555;
  --ink-soft:#888;
  --white:#fff;
  --rule:#ddd;
}
*{box-sizing:border-box;margin:0;padding:0}
html,body{width:1200px;height:3000px;overflow:hidden}
body{font-family:"Open Sans",Arial,sans-serif;color:var(--ink);position:relative;
  background:linear-gradient(180deg,var(--sky-top) 0,var(--blue) 500px,var(--sky-low) 1300px,var(--lime-soft) 1900px,var(--grass) 2500px,var(--grass-dark) 3000px)}
.hills{position:absolute;left:0;top:1700px;width:1200px;height:1000px}
.abs{position:absolute}
/* header */
.brand{left:100px;top:26px;display:flex;align-items:center;gap:12px}
.brand-dot{width:46px;height:46px;border-radius:50%;background:var(--pink)}
.brand-name{font-size:30px;font-weight:700;color:var(--white);line-height:1.05;width:220px}
.nav{left:277px;top:98px;width:823px;height:46px;background:var(--nav);border-radius:4px;display:flex}
.nav a{flex:1;display:flex;align-items:center;justify-content:center;font-size:14px;font-weight:600;color:#3d4a10;text-decoration:none;border-right:1px solid #c9c52c}
.nav a:last-child{border-right:0}
/* hero */
.hero{left:100px;top:200px;width:1000px;height:370px;border:6px solid var(--white);border-radius:4px;overflow:hidden}
.hero-photo{width:100%;height:100%;background:linear-gradient(180deg,#7cc5ef 0,#cfeafb 40%,#8cc63f 62%,#4e8f22 100%)}
.hero-card{position:absolute;right:40px;top:40px;width:330px;padding:20px 24px;background:rgba(1,146,205,.78);color:var(--white)}
.hero-card h2{font-size:24px;font-weight:700;margin-bottom:10px}
.hero-card p{font-size:13px;line-height:1.55;margin-bottom:14px}
.btn-dark{display:inline-block;background:#1b3f66;color:var(--white);font-size:13px;padding:6px 14px;border-radius:3px}
.arrow{position:absolute;top:165px;width:34px;height:34px;border-radius:50%;background:rgba(255,255,255,.6)}
.tabs{left:190px;top:524px;display:flex;gap:26px}
.tab{width:200px;height:62px;background:var(--orange-dark);border-radius:4px;display:flex;align-items:center;gap:12px;padding-left:14px;color:var(--white);font-size:16px;font-weight:600}
.tab i{width:34px;height:34px;border-radius:50%;background:#fff3}
/* main panel */
.panel{left:100px;top:606px;width:1000px;height:2010px;background:var(--white)}
.features{position:absolute;left:0;top:40px;width:1000px;display:flex;justify-content:space-around}
.feature{width:260px;text-align:center}
.tile{width:210px;height:210px;border-radius:30px;margin:0 auto 110px}
.tile.learn{background:var(--teal)}
.tile.create{background:var(--gold)}
.tile.share{background:var(--orange)}
.feature h3{color:var(--blue-deep);font-size:19px;font-weight:700;margin-bottom:10px;letter-spacing:.5px}
.feature p{font-size:13.5px;line-height:1.6;color:var(--ink);min-height:150px}
.btn-small{display:inline-block;background:var(--orange);color:var(--white);font-size:11px;padding:4px 12px;border-radius:2px}
.welcome{position:absolute;left:30px;top:660px;width:940px;height:340px}
.video{position:absolute;left:0;top:0;width:500px;height:290px;background:linear-gradient(135deg,#c8a0b5,#6c8fb8 60%,#2d4261)}
.video-bar{position:absolute;left:0;bottom:0;width:100%;height:28px;background:rgba(0,0,0,.55)}
.welcome h2{position:absolute;left:530px;top:-8px;color:var(--pink);font-size:38px;font-weight:700;line-height:1.15}
.welcome p{position:absolute;left:530px;top:100px;width:410px;font-size:13px;line-height:1.6}
.btn-blue{position:absolute;left:530px;top:312px;background:var(--blue-deep);color:var(--white);font-size:15px;padding:8px 20px;border-radius:3px}
.divider{position:absolute;left:30px;top:1030px;width:940px;border-top:1px solid var(--rule)}
.sec-title{position:absolute;left:30px;color:var(--blue-deep);font-size:24px;font-weight:700;letter-spacing:.5px}
.pill{position:absolute;right:30px;background:#e2e2e2;color:#888;font-size:11px;padding:3px 12px;border-radius:2px}
.cards{position:absolute;left:30px;top:1118px;width:940px;display:flex;justify-content:space-between}
.card{width:290px;height:270px;border:1px solid #e6e6e6;background:var(--white)}
.card-photo{height:112px}
.card h4{color:var(--blue-deep);font-size:17px;font-weight:600;margin:12px 14px 6px}
.card p{font-size:13px;line-height:1.55;margin:0 14px 14px}
.card .btn-small{margin-left:14px;font-size:12px;padding:5px 14px}
.quote{position:absolute;left:30px;top:1490px;width:940px;height:190px;border:1px solid #e6e6e6;padding:28px 30px 0 110px}
.quote svg{position:absolute;left:32px;top:30px}
.quote p{font-size:14px;line-height:1.6}
.quote .who{position:absolute;right:30px;bottom:24px;text-align:right;font-size:12px;color:var(--ink)}
.news{position:absolute;left:30px;top:1825px;width:940px;height:150px;border:1px solid #e6e6e6;padding:22px 26px;font-size:13px;line-height:1.6}
/* footer */
.footer{left:100px;top:2640px;width:1000px;height:360px;color:var(--white)}
.cols{display:flex;justify-content:space-between;padding-top:20px}
.col{width:290px;font-size:13px;line-height:1.65}
.col h5{font-size:15px;font-weight:700;letter-spacing:.5px;margin-bottom:12px;color:var(--yellow)}
.pin{display:flex;align-items:center;gap:6px;font-weight:700;margin-top:8px}
.social{display:flex;gap:16px;margin-top:22px}
.social i{width:38px;height:38px;border-radius:4px;background:#3c6b17}
.copyright{position:absolute;right:0;bottom:14px;width:290px;font-size:12px;border-top:1px solid #ffffff55;padding-top:8px}
</style>
</head>
<body>
<svg class="hills" viewBox="0 0 1200 1000" aria-hidden="true">
  <path d="M0 380 Q160 300 320 360 L320 1000 L0 1000Z" fill="#9bc83a"/>
  <path d="M880 420 Q1040 320 1200 360 L1200 1000 L880 1000Z" fill="#9bc83a"/>
  <path d="M0 620 Q240 520 500 600 Q800 690 1200 560 L1200 1000 L0 1000Z" fill="#86b932"/>
</svg>

<header>
  <div class="abs brand"><span class="brand-dot"></span><span class="brand-name">Maple Nook Kidcare</span></div>
  <nav class="abs nav">
    <a>Home ▾</a><a>About Us</a><a>Services</a><a>Enrollment</a><a>Policies</a><a>Contact Us</a><a>Photos</a><a>Testimonials</a>
  </nav>
</header>

<section class="abs hero">
  <div class="hero-photo" role="img" aria-label="Photo of a child running across a green playground under a blue sky"></div>
  <div class="hero-card">
    <h2>A Caring Environment</h2>
    <p>Lorem ipsum dolor sit amet, consectetuer adipiscing elit, sed diam nonummy nibh euismod tincidunt ut laoreet dolore magna aliquam erat volutpat. Ut wisi enim ad minim veniam, quis nostrud exerci tation ullamcorper suscipit lobortis nisl ut aliquip ex ea commodo.</p>
    <span class="btn-dark">Check it out</span>
  </div>
  <span class="arrow" style="left:14px"></span>
  <span class="arrow" style="right:14px"></span>
</section>

<div class="abs tabs">
  <div class="tab"><i></i>Playgrounds</div>
  <div class="tab"><i></i>Activities</div>
  <div class="tab"><i></i>Teachers</div>
  <div class="tab"><i></i>Programmes</div>
</div>

<main class="abs panel">
  <div class="features">
    <div class="feature">
      <div class="tile learn" role="img" aria-label="Illustration of an open book"></div>
      <h3>LEARNING</h3>
      <p>We develop age-appropriate activities that introduce and strengthen academic and social skills.</p>
      <span class="btn-small">Read more</span>
    </div>
    <div class="feature">
      <div class="tile create" role="img" aria-label="Illustration of a graduation cap"></div>
      <h3>CREATIVITY</h3>
      <p>We offer children a wide range of creative opportunities including art projects, toddler yoga lessons, afternoon tea parties, dress up play, and a large selection of books and games.</p>
      <span class="btn-small">Read more</span>
    </div>
    <div class="feature">
      <div class="tile share" role="img" aria-label="Illustration of sharing toys"></div>
      <h3>SHARING</h3>
      <p>We strive to include enrichment activities that extend your child's understanding of the world and their role in it. During our tea parties, for instance, we teach and emphasize good manners so that your child can learn their benefits as they grow.</p>
      <span class="btn-small">Read more</span>
    </div>
  </div>

  <div class="welcome">
    <div class="video" role="img" aria-label="Video still of children playing in a classroom"><div class="video-bar"></div></div>
    <h2>Welcome to<br>Maple Nook Kidcare</h2>
    <p>Welcome to Maple Nook Kidcare, a licensed Group Family Day Care in Brookfield's beautiful Upper Side. We are located on a pretty, tree-lined street on the Upper Side between Elm and Oak Street, just a short walk from the local bus line and a quick ride from town. We offer flexible hourly care, making it as easy as possible for busy parents to arrange their children's care.</p>
    <p style="top:262px">Please call to learn more about us and we hope you will visit us soon!</p>
    <span class="btn-blue">View More ›</span>
  </div>

  <div class="divider"></div>
  <h3 class="sec-title" style="top:1060px">DAYCARE AT A GLANCE</h3>
  <span class="pill" style="top:1068px">Read more</span>
  <div class="cards">
    <article class="card">
      <div class="card-photo" role="img" aria-label="Photo of children building with blocks at a table" style="background:linear-gradient(135deg,#e9c39a,#b98c5f)"></div>
      <h4>Daycare Experience</h4>
      <p>We develop age-appropriate activities that introduce and strengthen academic and social skills.</p>
      <span class="btn-small">Learn more ›</span>
    </article>
    <article class="card">
      <div class="card-photo" role="img" aria-label="Photo of children learning together" style="background:linear-gradient(135deg,#bcd4ea,#e8c6b2)"></div>
      <h4>Active Learning</h4>
      <p>We develop age-appropriate activities that introduce and strengthen academic and social skills.</p>
      <span class="btn-small">Learn more ›</span>
    </article>
    <article class="card">
      <div class="card-photo" role="img" aria-label="Photo of a teacher reading with a child" style="background:linear-gradient(135deg,#f2b35a,#c0683a)"></div>
      <h4>Our Approach</h4>
      <p>We develop age-appropriate activities that introduce and strengthen academic and social skills.</p>
      <span class="btn-small">Learn more ›</span>
    </article>
  </div>

  <h3 class="sec-title" style="top:1440px">WHAT OUR CUSTOMER SAYS</h3>
  <div class="quote">
    <svg width="50" height="40" viewBox="0 0 50 40" aria-hidden="true"><path d="M4 38V20Q4 6 18 2v7q-6 3-6 11h6v18Zm26 0V20q0-14 14-18v7q-6 3-6 11h6v18Z" fill="#bbb"/></svg>
    <p>Maple Nook Kidcare is affectionate, warm and caring. It has an excellent environment for young kids, which involve all types of learning and play activities.</p>
    <div class="who"><strong>Anne</strong><br>Customer</div>
  </div>

  <h3 class="sec-title" style="top:1775px">NEWS</h3>
  <span class="pill" style="top:1783px">Read more</span>
  <div class="news">We are thrilled to have found a new cheerful space with lots of room for new play equipment such as a toddler slide, sand/water activity table and more! Updated programs and services as we say goodbye to Winter and hello to Spring.</div>
</main>

<footer class="abs footer">
  <div class="cols">
    <div class="col">
      <h5>AT A GLANCE</h5>
      “ Get a delicious gift for your kids, they will love it with our new website design”<br>yesterday
      <div class="social"><i aria-label="Social link"></i><i aria-label="Social link"></i><i aria-label="Social link"></i></div>
    </div>
    <div class="col">
      <h5>CONTACT US</h5>
      Dana Whitfield<br>27 Orchard Lane<br>Brookfield, NY 10999<br>Phone: (555) 014-2280<br>Email: hello@maplenookkidcare.example
      <div class="pin"><svg width="14" height="18" viewBox="0 0 14 18" aria-hidden="true"><path d="M7 0a7 7 0 0 1 7 7c0 5-7 11-7 11S0 12 0 7a7 7 0 0 1 7-7Z" fill="#f29a1f"/><circle cx="7" cy="7" r="2.5" fill="#fff"/></svg>Get Directions</div>
    </div>
    <div class="col">
      <h5>TWEETS</h5>
      “ Get a delicious gift from our director Dana, as she's well prepared to launch this new website design”<br>yesterday
      <div class="social"><i aria-label="Social link"></i><i aria-label="Social link"></i><i aria-label="Social link"></i></div>
    </div>
  </div>
  <div class="copyright">© 2014 Maple Nook Kidcare</div>
</footer>
</body>
</html>
```